Education Certificate

We need a modern yet professional Certificate for those who successfully pass / complete our online Training course.

There are various courses but ONE certificate design required.

the certificate needs to look extremely professional and of value.

```html
<!DOCTYPE html>
<html lang="en">
<head>
<meta charset="utf-8">
<title>Certificate of Achievement</title>
<link rel="stylesheet" href="https://fonts.googleapis.com/css2?family=Arimo:wght@400;600&family=Bodoni+Moda:wght@500&family=Great+Vibes&family=Tinos&display=swap">
<style>
  :root {
    --backdrop: #dcdcdc;
    --paper: #ffffff;
    --navy: #25326d;
    --gold: #f5d20c;
    --gold-deep: #e8b923;
    --ink: #111111;
  }
  html, body {
    margin: 0;
    width: 1200px;
    height: 1200px;
    overflow: hidden;
    background: var(--backdrop);
  }
  .certificate { display: block; width: 1200px; height: 1200px; }
  .paper { fill: var(--paper); }
  .navy { fill: var(--navy); }
  .gold { fill: var(--gold); }
  .frame-outer { fill: none; stroke: var(--gold); stroke-width: 7; }
  .frame-inner { fill: none; stroke: var(--gold); stroke-width: 2.5; }
  .rule { stroke: var(--gold); stroke-width: 2.5; }
  .sign-line { stroke: var(--ink); stroke-width: 2.5; }
  .title { font-family: "Bodoni Moda", "Didot", serif; font-weight: 500; font-size: 108px; fill: var(--ink); letter-spacing: 2px; }
  .subtitle { font-family: "Arimo", Arial, sans-serif; font-size: 50px; fill: var(--ink); letter-spacing: 5px; }
  .presented { font-family: "Arimo", Arial, sans-serif; font-size: 48px; fill: var(--ink); letter-spacing: 5px; }
  .recipient { font-family: "Great Vibes", cursive; font-size: 128px; fill: var(--ink); letter-spacing: 3px; }
  .course { font-family: "Tinos", "Times New Roman", serif; font-size: 37px; fill: var(--ink); letter-spacing: 0.5px; }
  .body-copy { font-family: "Arimo", Arial, sans-serif; font-size: 23.5px; fill: var(--ink); }
  .label { font-family: "Arimo", Arial, sans-serif; font-size: 22px; fill: var(--ink); }
  .seal-ring { fill: var(--paper); stroke: var(--gold-deep); stroke-width: 6; }
  .seal-name { font-family: "Arimo", Arial, sans-serif; font-weight: 600; font-size: 21px; fill: var(--navy); letter-spacing: 1px; }
</style>
</head>
<body>
<svg class="certificate" viewBox="0 0 1932 1932" xmlns="http://www.w3.org/2000/svg">
  <defs>
    <filter id="paper-shadow" x="-5%" y="-5%" width="110%" height="115%">
      <feDropShadow dx="0" dy="6" stdDeviation="10" flood-color="#000" flood-opacity="0.35"/>
    </filter>
  </defs>

  <rect class="paper" x="77" y="335" width="1778" height="1267" filter="url(#paper-shadow)"/>

  <g class="frames">
    <rect class="frame-outer" x="157" y="410" width="1608" height="1122" rx="78"/>
    <rect class="frame-inner" x="200" y="447" width="1523" height="1046" rx="70"/>
  </g>

  <g class="corner corner-top-left">
    <polygon class="navy" points="77,335 515,335 77,752"/>
    <polygon class="gold" points="297,462 329,462 77,700 77,668"/>
    <polygon class="gold" points="529,335 587,335 77,820 77,762"/>
  </g>
  <g class="corner corner-bottom-right">
    <polygon class="navy" points="1855,1185 1855,1602 1418,1602"/>
    <polygon class="gold" points="1855,1238 1855,1270 1632,1480 1600,1480"/>
    <polygon class="gold" points="1855,1118 1855,1176 1405,1602 1347,1602"/>
  </g>

  <text class="title" x="970" y="583" text-anchor="middle">CERTIFICATE</text>

  <g class="ribbon">
    <line class="rule" x1="663" y1="614" x2="1283" y2="614"/>
    <polygon class="gold" points="663,626 1281,626 1262,665 1283,704 663,704 682,665"/>
    <line class="rule" x1="663" y1="716" x2="1283" y2="716"/>
    <text class="subtitle" x="970" y="686" text-anchor="middle">OF ACHIEVEMENT</text>
  </g>

  <text class="presented" x="968" y="835" text-anchor="middle">Proudly Presented To</text>
  <text class="recipient" x="968" y="978" text-anchor="middle">Name Surname</text>

  <text class="course" x="966" y="1103" text-anchor="middle">LOREM IPSUM DOLOR SIT AMET, CONSECTETUR ADIPISCING ELIT</text>
  <text class="body-copy" text-anchor="middle">
    <tspan x="963" y="1181">Lorem ipsum dolor sit amet, consectetur adipiscing elit. Mauris elit enim, egestas ut libero sit amet, ultrices mattis ex.</tspan>
    <tspan x="963" y="1216">Quisque id faucibus metus. Mauris sapien nunc, ultrices id tortor sed, euismod pellentesque mi. Nullam sollicitudin</tspan>
    <tspan x="963" y="1251">lorem tellus, vel fermentum odio sodales vel.</tspan>
  </text>

  <g class="signatures">
    <line class="sign-line" x1="429" y1="1408" x2="798" y2="1408"/>
    <text class="label" x="616" y="1436" text-anchor="middle">Date</text>
    <line class="sign-line" x1="1142" y1="1408" x2="1511" y2="1408"/>
    <text class="label" x="1326" y="1436" text-anchor="middle">Signature</text>
  </g>

  <g class="seal">
    <circle class="gold" cx="971" cy="1385" r="91"/>
    <circle class="seal-ring" cx="971" cy="1385" r="72"/>
    <text class="seal-name" x="971" y="1392" text-anchor="middle">VELTRANA</text>
  </g>
</svg>
</body>
</html>
```